Box insert for packaging of junior girls briefs

Need a insert to fit into our girls briefs packaging. Box is made of frosted plastic and measures 6 inches in width, 5 inches in height and 1.5 inches thick.

Box will have a open top flip as seen in photo of frosted envelope, same goes for closure.

Attached is a photo of a blank paper insert in a clear plastic box, that gives an idea as how I want it to look when inserted into the box. Note the small cutout of a brief to show what style this is. I would need to have same thing for hipster and bikini.
Design on packaging needs to be clean and sharp and appealing to junior girls and adults in their low 20's. Needs to be sophisticated but not provocative.
I'm uploading a EPS file of our logo. Basic logo layout should remain the same, however I'd like to see some creativity in making the logo more playful and young looking.
The front of the insert should have minimal information, maybe just size.
The back should contain information like website, contents, small size chart and country of origin (do in sample text).
Top of insert should have style number, size, logo and barcode. It can also have a picture (not cut out) of item style.

UPDATE: The front of the insert refers to the taller part and the back refers to the shorter part.

Plastic

• Must use our logo. It has been uploaded. Basic layout need to stay the same but you can change around the font and make it more playful. I might even consider a different color if it feels right.

```html
<!DOCTYPE html>
<html lang="en">
<head>
<meta charset="utf-8">
<title>Lumari Panties – Box Insert, Size M</title>
<link href="https://fonts.googleapis.com/css2?family=Archivo+Black&family=Source+Sans+3:wght@300;400;600;700&display=swap" rel="stylesheet">
<style>
  :root {
    --backdrop: #6f7fcb;
    --magenta: #a8185e;
    --magenta-light: #bd3a78;
    --pink-title: #f07cbf;
    --pink-swoosh: #e5409a;
    --pink-swoosh-light: #f868b8;
    --blush: #fbe2f0;
    --orange: #f39a2c;
    --logo-ink: #2e2a2c;
    --white: #ffffff;
  }
  * { box-sizing: border-box; margin: 0; padding: 0; }
  html, body {
    width: 900px; height: 1200px; overflow: hidden;
    background: var(--backdrop);
    font-family: "Source Sans 3", Arial, sans-serif;
  }
  .canvas { position: relative; width: 900px; height: 1200px; }

  .insert {
    position: absolute;
    left: 119px; top: 214px;
    width: 662px; height: 772px;
    transform: scale(1.15);
    transform-origin: center;
    box-shadow: 0 6px 18px rgba(40, 30, 80, .25);
  }

  .panel {
    position: absolute; left: 0; width: 662px; overflow: hidden;
    background: linear-gradient(90deg, var(--magenta) 0%, var(--magenta-light) 70%, var(--magenta) 100%);
  }
  .panel + .panel { border-top: 1px solid rgba(255,255,255,.18); }

  /* Back panel – printed upside down */
  .panel-back { top: 0; height: 165px; }
  .back-content {
    position: absolute; inset: 0;
    transform: rotate(180deg);
    color: var(--white);
  }
  .composition {
    position: absolute; left: 12px; top: 18px; width: 335px;
    font-size: 7px; line-height: 10px; letter-spacing: .1px;
    text-transform: uppercase;
  }
  .care-icons {
    position: absolute; left: 40px; top: 118px;
    display: flex; gap: 8px; align-items: center;
  }
  .care-icons svg { width: 18px; height: 16px; }
  .website {
    position: absolute; left: 148px; top: 144px;
    font-size: 8px; font-weight: 600; letter-spacing: .3px;
  }
  .size-chart {
    position: absolute; left: 310px; top: 14px;
    border: 1px solid var(--white); border-radius: 6px;
    padding: 6px 8px;
  }
  .size-chart table { border-collapse: separate; border-spacing: 5px 3px; }
  .size-chart td {
    width: 33px; height: 15px; text-align: center;
    font-size: 8px; color: var(--white);
  }
  .size-chart td.boxed, .size-chart th {
    border: 1px solid var(--white); border-radius: 2px;
  }
  .size-chart th { width: 42px; font-size: 8px; font-weight: 600; }

  /* Top panel */
  .panel-top { top: 165px; height: 165px; }
  .brand-name {
    position: absolute; left: 50px; top: 58px;
    font-weight: 300; font-size: 56px; letter-spacing: 1px;
    color: var(--logo-ink); line-height: 1;
  }
  .top-size {
    position: absolute; right: 26px; top: 38px;
    font-size: 28px; font-weight: 600; color: var(--orange);
  }

  /* Front panel */
  .panel-front { top: 330px; height: 442px; }
  .product-title {
    position: absolute; left: 30px; top: 4px;
    font-family: "Archivo Black", "Arial Black", sans-serif;
    font-size: 138px; line-height: 1; letter-spacing: -3px;
    color: var(--pink-title);
  }
  .style-cutout {
    position: absolute; left: 200px; top: 150px;
    width: 250px; height: 292px;
    background: linear-gradient(100deg, var(--pink-swoosh) 0%, var(--pink-swoosh-light) 65%, var(--blush) 100%);
  }
  .butterfly-art {
    position: absolute; left: 380px; top: 160px;
    width: 270px; height: 262px;
    background:
      radial-gradient(circle at 30% 35%, rgba(60,200,240,.9), transparent 45%),
      radial-gradient(circle at 72% 40%, rgba(255,220,40,.85), transparent 42%),
      radial-gradient(circle at 50% 78%, rgba(240,60,150,.85), transparent 50%),
      #1d1a24;
  }
  .front-size {
    position: absolute; left: 42px; bottom: 12px;
    font-size: 44px; font-weight: 600; color: var(--white);
    line-height: 1;
  }
</style>
</head>
<body>
<main class="canvas">
  <section class="insert" aria-label="Box insert, flat layout">

    <div class="panel panel-back">
      <div class="back-content">
        <p class="composition">
          95% Cotton / 5% Elastane<br>
          95% Baumwolle / Coton / Cotone / Algodón / Katoen<br>
          5% Elasthan / Élasthanne / Elastano / Elastaan<br>
          Single jersey elastic / Jersey élastique / Jersey elastico<br>
          Medium leg / Jambe moyenne / Gamba media<br>
          Compact cotton · Made in Portugal
        </p>
        <div class="care-icons" aria-label="Care symbols">
          <svg viewBox="0 0 18 16"><path d="M2 4 L16 4 L14 14 L4 14 Z" fill="none" stroke="#fff" stroke-width="1.2"/><text x="9" y="12" font-size="6" fill="#fff" text-anchor="middle">60</text></svg>
          <svg viewBox="0 0 18 16"><path d="M2 14 L9 2 L16 14 Z M3 3 L15 15 M15 3 L3 15" fill="none" stroke="#fff" stroke-width="1.2"/></svg>
          <svg viewBox="0 0 18 16"><rect x="2" y="1" width="14" height="14" fill="none" stroke="#fff" stroke-width="1.2"/><circle cx="9" cy="8" r="4.5" fill="none" stroke="#fff" stroke-width="1.2"/></svg>
          <svg viewBox="0 0 18 16"><path d="M2 12 L4 5 L14 5 L16 12 Z" fill="none" stroke="#fff" stroke-width="1.2"/><circle cx="9" cy="9" r="1" fill="#fff"/></svg>
          <svg viewBox="0 0 18 16"><circle cx="9" cy="8" r="7" fill="none" stroke="#fff" stroke-width="1.2"/><text x="9" y="11" font-size="8" fill="#fff" text-anchor="middle">F</text></svg>
          <svg viewBox="0 0 18 16"><circle cx="9" cy="8" r="7" fill="#fff"/></svg>
          <svg viewBox="0 0 18 16"><path d="M9 2 L15 12 L3 12 Z" fill="none" stroke="#fff" stroke-width="1.4"/></svg>
          <svg viewBox="0 0 18 16"><circle cx="9" cy="8" r="7" fill="#fff"/></svg>
        </div>
        <p class="website">WWW.LUMARI.COM</p>

        <div class="size-chart">
          <table>
            <tr><th></th><td class="boxed">XXS</td><td class="boxed">XS</td><td class="boxed">S</td><td class="boxed">M</td><td class="boxed">L</td><td class="boxed">XL</td></tr>
            <tr><th>D,CH,A</th><td>34</td><td>36/38</td><td>40/42</td><td>44/46</td><td>48/50</td><td>52/54</td></tr>
            <tr><th>F,I</th><td>34/36</td><td>38/42</td><td>44/46</td><td>48/50</td><td>52/54</td><td>56/58</td></tr>
            <tr><th>UK</th><td>32</td><td>34/36</td><td>38/40</td><td>42/44</td><td>46/48</td><td>50/52</td></tr>
            <tr><th>US</th><td>2</td><td>4</td><td>5</td><td>6</td><td>7</td><td>8</td></tr>
          </table>
        </div>
      </div>
    </div>

    <div class="panel panel-top">
      <p class="brand-name">LUMARI</p>
      <p class="top-size">Size: M</p>
    </div>

    <div class="panel panel-front">
      <h1 class="product-title">Panties</h1>
      <div class="style-cutout" role="img" aria-label="Pink brief-shaped cutout window showing the garment style"></div>
      <div class="butterfly-art" role="img" aria-label="Illustration of a rainbow-coloured butterfly with black wing edges"></div>
      <p class="front-size">Size: M</p>
    </div>

  </section>
</main>
</body>
</html>
```